Granite, Zinc and Clay Roofing LLC needs a new business card

I need a new business card because I have a new address.
I do slate copper and tile roofs. My webpage is: www.granitezincandclayroofing.example

```html
<!DOCTYPE html>
<html lang="en">
<head>
<meta charset="utf-8">
<title>Granite, Zinc and Clay Roofing LLC – Business Card</title>
<link href="https://fonts.googleapis.com/css2?family=Mukta:wght@400;500;600&display=swap" rel="stylesheet">
<style>
  :root {
    --page-bg: #dcdcdc;
    --card-white: #ffffff;
    --brand-blue: #4f9ecf;
    --ink: #0c0c0c;
    --text: #1a1a1a;
  }
  html, body { margin: 0; padding: 0; }
  body {
    width: 1200px; height: 1059px; overflow: hidden;
    background: var(--page-bg);
    font-family: "Mukta", sans-serif;
    position: relative;
  }
  .card {
    position: absolute;
    border-radius: 24px;
    overflow: hidden;
  }
  .card-front {
    left: 256px; top: 100px; width: 688px; height: 391px;
    background: var(--card-white);
  }
  .card-back {
    left: 253px; top: 537px; width: 694px; height: 394px;
    background: var(--brand-blue);
  }
  .front-wave { position: absolute; left: 0; top: 0; width: 688px; height: 391px; }
  .holder-name {
    position: absolute; left: 30px; top: 50px; margin: 0;
    font-size: 27px; font-weight: 500; color: var(--brand-blue); line-height: 1;
  }
  .holder-role {
    position: absolute; left: 30px; top: 86px; margin: 0;
    font-size: 17px; color: var(--text); line-height: 1;
  }
  .address {
    position: absolute; left: 30px; top: 150px; margin: 0;
    font-size: 16px; font-style: normal; color: var(--text); line-height: 20px;
  }
  .contact-list {
    position: absolute; left: 30px; top: 215px; margin: 0; padding: 0; list-style: none;
    font-size: 16px; color: var(--text); line-height: 23.5px;
  }
  .contact-list li { display: flex; align-items: center; gap: 7px; white-space: nowrap; }
  .contact-icon { width: 13px; height: 13px; flex: none; }
  .front-brand {
    position: absolute; left: 400px; top: 150px; width: 270px;
    display: flex; align-items: center; gap: 10px;
  }
  .brand-square { width: 16px; height: 16px; background: var(--brand-blue); flex: none; }
  .brand-name {
    margin: 0; font-size: 22px; font-weight: 600; color: var(--ink); line-height: 1.1;
  }
  .back-brand {
    position: absolute; left: 0; right: 0; top: 0; bottom: 0;
    display: flex; align-items: center; justify-content: center;
  }
  .back-brand .brand-name { font-size: 40px; text-align: center; width: 520px; line-height: 1.1; }
</style>
</head>
<body>
  <section class="card card-front">
    <svg class="front-wave" viewBox="0 0 688 391" aria-hidden="true">
      <path d="M0 372 C60 340 110 330 160 331 C300 333 430 372 555 368 C620 366 660 354 688 340 L688 391 L0 391 Z" fill="var(--brand-blue)"/>
      <path d="M2 366 C50 330 100 316 160 315 C300 318 430 362 555 364 C620 364 660 350 685 338 C660 352 620 362 555 361 C430 358 300 328 160 328 C100 328 55 340 2 366 Z" fill="var(--ink)"/>
    </svg>
    <h1 class="holder-name">Laszlo (Leo) Varga</h1>
    <p class="holder-role">Owner</p>
    <address class="address">2870 Millbrook Rd<br>Millbrook, OH 44000</address>
    <ul class="contact-list">
      <li>
        <svg class="contact-icon" viewBox="0 0 16 16" aria-hidden="true"><path d="M2 7 C2 3 14 3 14 7 L11 8 L10 6 L6 6 L5 8 Z M4 9 L12 9 L14 14 L2 14 Z" fill="var(--brand-blue)"/></svg>
        (555) 014-2290
      </li>
      <li>
        <svg class="contact-icon" viewBox="0 0 16 16" aria-hidden="true"><rect x="1" y="3" width="14" height="10" rx="1" fill="var(--brand-blue)"/><path d="M1 4 L8 9 L15 4" stroke="#fff" stroke-width="1.3" fill="none"/></svg>
        info@granitezincandclayroofing.example
      </li>
      <li>
        <svg class="contact-icon" viewBox="0 0 16 16" aria-hidden="true"><circle cx="8" cy="8" r="7" fill="none" stroke="var(--brand-blue)" stroke-width="1.5"/><path d="M8 1 C5 5 5 11 8 15 M8 1 C11 5 11 11 8 15 M1 8 L15 8" stroke="var(--brand-blue)" stroke-width="1.2" fill="none"/></svg>
        www.granitezincandclayroofing.example
      </li>
    </ul>
    <div class="front-brand">
      <span class="brand-square"></span>
      <p class="brand-name">Granite, Zinc and Clay Roofing LLC</p>
    </div>
  </section>

  <section class="card card-back">
    <div class="back-brand">
      <p class="brand-name">Granite, Zinc and Clay Roofing LLC</p>
    </div>
  </section>
</body>
</html>
```